Web design for Crowdfunding site HopeWingsHub.com

We need a web design for christian crowdfunding website. Here is the challenge: We need responsive layout that is targeted first in iPad size of screen. It should also scale somehow down to iPhone size of screens. Web layout can be about the same size as iPad screen.

Screens should work so that main page scrolls not but only certain part of the screen scrolls and always one "page" at time. We can implement these "scrolls" then later with javascript but now we need only design. The challenge is to create this kind of hybrid website / app look.

Target is at first to raise funds to orphan people needing about $40 per month for their living and education. There is always some organization which takes care of these kids. Later there will be other christian missions included. At first we are looking to find monthly supporters.

You can be as creative as you want :) As you see from the look and feel sector, I am not looking any same traditional look which many "help kids" sites have. I am looking to reach now younger generation and therefore iPad and mobile are the main screen sizes.

Inspirational designs:
- https://examplegallery.test/profiles/studiokavrel/designs/381264?from=%2Fbrowse%2Fxhr%2Fdesigns%3Fcategory%3Dmobile-app-design
- http://www.pixelforum.test/design/8264190 Clear, simple visuals
- http://www.pixelforum.test/design/7421953 Header
- http://www.pixelforum.test/design/6392017 Contrast in the colors, i think is powerfull

Some terms could be: Kids play, kids are learning (in the school). No static posture but living like kids are. I wonder also how we could also add little bit gaming style even though the question is of reali life of real people. Giving should be rewarding.

Target Market(s)

People who want help other people.

Industry/Entity Type

Christian

Number of Pages Required

4 page

Requirements
Must have
• Homepage. Mission page (In my wireframes it was one kid).
Nice to have
• Other pages and some idea how to scroll. 4 pages is no must. If you feel easy, please give first some draft and I give comments on that.

```html
<!DOCTYPE html>
<html lang="en">
<head>
<meta charset="utf-8">
<title>HopeWingsHub — Christian Crowd Funding</title>
<link href="https://fonts.googleapis.com/css2?family=Montserrat:wght@300;400;500;700;800&display=swap" rel="stylesheet">
<style>
  :root {
    --amber: #ffb300;
    --amber-deep: #ff9800;
    --white: #ffffff;
    --ink: #141414;
    --footer-bg: #161616;
    --footer-text: #4a4a4a;
    --avatar-fill: #9a9a9a;
    --avatar-ring: #d8d8d8;
    --photo-dark: #1e1d1b;
    --photo-mid: #3a3733;
  }
  * { box-sizing: border-box; margin: 0; padding: 0; }
  html, body { width: 1200px; height: 900px; overflow: hidden; background: var(--ink); }
  body { font-family: "Montserrat", Arial, sans-serif; color: var(--white); }

  .page { position: relative; width: 1200px; height: 900px; overflow: hidden; }

  .site-header {
    position: absolute; top: 0; left: 0; width: 1200px; height: 97px;
    background: var(--amber); z-index: 3;
  }
  .menu-toggle { position: absolute; left: 57px; top: 35px; width: 36px; height: 28px; display: flex; flex-direction: column; justify-content: space-between; }
  .menu-toggle span { display: block; height: 5px; background: var(--white); }
  .mission-link { position: absolute; left: 108px; top: 38px; font-weight: 700; font-size: 16px; letter-spacing: 0.2px; }
  .search-icon { position: absolute; left: 270px; top: 40px; }
  .brand { position: absolute; left: 0; right: 0; top: 28px; text-align: center; font-weight: 700; font-size: 33px; letter-spacing: 0.5px; }
  .login-button {
    position: absolute; left: 940px; top: 28px; width: 105px; height: 42px;
    background: var(--amber-deep); border: 1px solid var(--white); border-radius: 4px;
    font-size: 16px; font-weight: 500; display: flex; align-items: center; justify-content: center;
  }
  .signup-link { position: absolute; left: 1076px; top: 39px; font-size: 16px; font-weight: 500; }

  .hero { position: absolute; top: 97px; left: 0; width: 1200px; height: 739px; }
  .hero-photo {
    position: absolute; inset: 0;
    background: radial-gradient(ellipse at 55% 55%, var(--photo-mid) 0%, var(--photo-dark) 70%);
  }
  .network { position: absolute; top: 0; left: 0; }

  .hero-copy {
    position: absolute; left: -2px; top: 170px; width: 860px;
    text-align: center; transform: rotate(-30deg); transform-origin: center center;
  }
  .hero-title { font-weight: 800; font-size: 42px; letter-spacing: 0.5px; line-height: 1.2; }
  .hero-title .accent { color: var(--amber); }
  .hero-text { font-weight: 300; font-size: 21px; line-height: 46px; margin-top: 6px; }

  .site-footer {
    position: absolute; left: 0; bottom: 0; width: 1200px; height: 64px;
    background: var(--footer-bg); display: flex; align-items: center; justify-content: center;
    color: var(--footer-text); font-size: 16px;
  }
</style>
</head>
<body>
<div class="page">
  <header class="site-header">
    <div class="menu-toggle"><span></span><span></span><span></span></div>
    <div class="mission-link">SEE THE MISSION</div>
    <svg class="search-icon" width="16" height="16" viewBox="0 0 16 16">
      <circle cx="6.5" cy="6.5" r="4.8" fill="none" stroke="#fff" stroke-width="2.4"/>
      <line x1="10" y1="10" x2="14.5" y2="14.5" stroke="#fff" stroke-width="2.8" stroke-linecap="round"/>
    </svg>
    <div class="brand">HOPEWINGSHUB</div>
    <div class="login-button">LOGIN</div>
    <div class="signup-link">SIGNUP</div>
  </header>

  <main class="hero">
    <div class="hero-photo" role="img" aria-label="Dark photograph of many hands stacked together in a circle"></div>

    <svg class="network" width="1200" height="739" viewBox="0 97 1200 739">
      <g stroke="#cfcfcf" stroke-width="1.2" stroke-dasharray="5 4" fill="none" opacity="0.8">
        <line x1="659" y1="435" x2="850" y2="312"/>
        <line x1="850" y1="312" x2="1068" y2="367"/>
        <line x1="1068" y1="367" x2="1022" y2="639"/>
        <line x1="838" y1="514" x2="1022" y2="639"/>
        <line x1="838" y1="514" x2="568" y2="639"/>
        <line x1="568" y1="639" x2="797" y2="717"/>
      </g>
      <defs>
        <g id="member">
          <circle r="53" fill="#2a2826" fill-opacity="0.35" stroke="#d8d8d8" stroke-width="1.5"/>
          <circle cy="-12" r="17" fill="#9a9a9a"/>
          <path d="M-36 34 Q-34 10 0 8 Q34 10 36 34 Z" fill="#9a9a9a"/>
        </g>
      </defs>
      <use href="#member" x="850" y="312"/>
      <use href="#member" x="1068" y="367"/>
      <use href="#member" x="659" y="435"/>
      <use href="#member" x="838" y="514"/>
      <use href="#member" x="568" y="639"/>
      <use href="#member" x="1022" y="639"/>
      <use href="#member" x="797" y="717"/>
    </svg>

    <div class="hero-copy">
      <h1 class="hero-title">CHRISTIAN <span class="accent">CROWD FUNDING</span></h1>
      <p class="hero-text">She has a name.He has dream.She hopes she would have a future. He is<br>like you.I USD a month will help her and him</p>
    </div>
  </main>

  <footer class="site-footer">Copyrights@2016Company Name, all rights reserved</footer>
</div>
</body>
</html>
```